Web Site Design for a Finance (lending) Company

We are opening a new subsidiary that focuses on lending money in the real estate industry. We need a web site designed to represent the business.

The business is lending money to real estate investors. A typical client/borrower will be looking to borrow money to buy a house, renovate it and then sell it at a profit, all within 12 months or less.

Company name is Brevand Finance. Our logo is attached.

Attached is a general outline for the web site. We're working on writing more text for each page but this should give you enough to get started with some ideas.

Competitor web site that I like a lot (as an example): https://quorvelfunding.com/. Many of the general items on this site match what we will need (description of loan programs, FAQ)

Target Market(s)

Real estate investors (generally individuals or small companies with just a few people) who are buying homes, renovating them and then selling them at a profit.

Industry/Entity Type

Finance

Coding

Coded - Design and coding required

Number of Pages Required

5+ page

Colors

Designer to choose colors to be used in the design.

Requirements
Must have
• Minimalist design. Clean lines without too much clutter. Some stock photography is ok but the photos should not be distracting. They should almost fade in to the background so that user can focus on the key information about what our company does instead. We are a finance company, not a design company, so the information about our products will be more interesting to site visitors than the art.
• Some minimalist examples from Snapboard:
• https://www.snapboard-example.com/explore/minimalist-web-design/
Nice to have
• If you search in seekly for "hard money lenders" you will find many examples of web sites from our competition. I have provided a link above to competitor web site that I like a lot.
• I have attached our logo in EPS format. Logo is green. Web site doesn't have to be green but it should be of a color that will work well with the logo.

```html
<!DOCTYPE html>
<html lang="en">
<head>
<meta charset="utf-8">
<title>Brevand Finance</title>
<link href="https://fonts.googleapis.com/css2?family=Open+Sans:wght@400;600;700;800&display=swap" rel="stylesheet">
<style>
:root{
  --green:#2f6b4c;
  --green-dark:#1f5337;
  --green-soft:#4f8a69;
  --ink:#2b2b2b;
  --muted:#6b6b6b;
  --line:#d9d9d9;
  --paper:#ffffff;
  --mist:#f1f1f1;
  --card:#e9e9e9;
  --card-dark:#9c9c9c;
}
*{box-sizing:border-box;margin:0;padding:0}
html,body{width:1200px;height:4826px;overflow:hidden}
body{position:relative;background:var(--paper);font-family:"Open Sans",Arial,sans-serif;color:var(--ink)}
.abs{position:absolute}
.btn{position:absolute;background:var(--green-dark);color:#fff;font-weight:700;font-size:15px;letter-spacing:1px;text-align:center;line-height:42px;height:42px;width:190px;border-radius:4px;text-transform:uppercase}
.section-title{position:absolute;left:0;width:1200px;text-align:center;font-size:21px;font-weight:600;color:var(--ink)}
.section-title .mark{display:inline-block;width:14px;height:14px;background:var(--green);margin-right:12px;vertical-align:1px}

/* header */
.site-header{top:0;left:0;width:1200px;height:106px;background:#fff}
.nav{position:absolute;top:44px;font-size:13px;font-weight:600;letter-spacing:.5px;text-transform:uppercase;color:var(--ink)}
.nav span{margin-right:34px}
.nav-left{left:110px}
.nav-right{left:760px}
.nav .apply{background:var(--green-dark);color:#fff;padding:6px 12px;border-radius:3px;margin-right:0}
.brand{position:absolute;top:30px;left:500px;width:200px;text-align:center;font-size:24px;font-weight:700;color:var(--green-dark)}
.brand-lg{font-size:30px}

/* hero */
.hero{top:106px;left:0;width:1200px;height:521px;background:linear-gradient(180deg,#8fa7bd 0%,#a4a29a 40%,#6f7a5c 75%,#55663f 100%)}
.hero-title{top:410px;left:0;width:1200px;text-align:center;color:#fff;font-size:34px;font-weight:800;text-transform:uppercase;text-shadow:0 2px 6px rgba(0,0,0,.4)}
.hero-sub{top:456px;left:0;width:1200px;text-align:center;color:#fff;font-size:19px;font-weight:700;text-transform:uppercase;text-shadow:0 2px 6px rgba(0,0,0,.4)}

/* loan cards */
.loan-card{top:621px;width:354px;height:289px;background:var(--card);text-align:center}
.loan-card.alt{background:var(--card-dark);color:#fff}
.loan-card svg{margin-top:40px}
.loan-name{font-size:26px;font-weight:700;color:#8e8e8e;letter-spacing:1px;margin-top:6px}
.loan-card.alt .loan-name{color:#fff}
.loan-desc{font-size:15px;line-height:22px;color:#666;padding:0 40px;margin-top:24px}
.loan-card.alt .loan-desc{color:#fff;font-weight:600}
.pin{position:absolute;top:12px;right:12px;width:26px;height:26px;border-radius:50%;background:#fff;opacity:.8}

/* fading backgrounds */
.fade-bg{left:0;width:1200px;background:linear-gradient(180deg,#fff 0%,#e3e3e3 30%,#ededed 70%,#fff 100%)}

/* services */
.service{top:1210px;width:250px;text-align:center}
.service svg{display:block;margin:0 auto}
.service h3{font-size:13px;font-weight:700;color:var(--green);margin-top:16px}
.service p{font-size:12px;line-height:17px;color:var(--muted);margin-top:6px}

/* case studies */
.case{top:1785px;width:364px;height:322px;background:var(--mist)}
.case .photo{height:210px}
.case h4{font-size:14px;font-weight:700;margin:12px 14px 4px;text-transform:uppercase}
.case p{font-size:12px;line-height:17px;color:var(--muted);margin:0 14px}

/* testimonials */
.testimonial-bg{top:2284px;left:0;width:1200px;height:531px;background:linear-gradient(180deg,#fff 0%,#dcdcdc 25%,#e6e6e6 75%,#fff 100%)}
.quote{top:2493px;width:330px;height:176px;background:var(--green-soft);color:#fff;border-radius:6px;padding:20px 22px 0 60px;font-size:13px;line-height:19px}
.quote .qmark{position:absolute;left:18px;top:12px;font-size:44px;font-weight:800;line-height:44px}
.person{top:2680px;font-size:17px;font-style:normal;font-weight:600}
.avatar{top:2660px;width:78px;height:78px;border-radius:50%;background:linear-gradient(180deg,#cfc3b6,#9e8d7d);border:4px solid #fff}

/* resources */
.resource{background:var(--mist)}
.resource .photo{width:100%}
.resource h4{font-size:14px;font-weight:700;margin:8px 14px 2px;text-transform:uppercase}
.resource p{font-size:12px;line-height:17px;color:var(--muted);margin:0 14px}

/* faq */
.faq{left:312px;width:579px}
.faq-q{height:30px;background:var(--green);color:#fff;border-radius:15px;font-size:13px;font-weight:600;line-height:30px;padding:0 18px;margin-bottom:10px;position:relative}
.faq-q::after{content:"";position:absolute;right:16px;top:10px;width:7px;height:7px;border-right:2px solid #fff;border-bottom:2px solid #fff;transform:rotate(45deg)}
.faq-open{background:var(--green);color:#fff;border-radius:15px;padding:8px 18px 10px;margin-bottom:10px;font-size:13px}
.faq-open b{display:block;font-weight:600;line-height:20px}
.faq-open span{display:block;font-size:12px;line-height:17px;opacity:.9}

/* footer */
.site-footer{top:4456px;left:0;width:1200px}
.f-col{position:absolute;top:0;font-size:13px;line-height:19px}
.f-col h5{font-size:14px;font-weight:700;text-transform:uppercase;margin-bottom:12px;letter-spacing:.5px}
.newsletter{display:flex;margin-top:4px}
.newsletter .field{width:150px;height:34px;border:1px solid #999;font-size:12px;line-height:32px;padding:0 8px;color:#777}
.newsletter .go{width:80px;height:34px;background:var(--green-dark);color:#fff;font-weight:700;font-size:13px;line-height:34px;text-align:center}
.contact-row{display:flex;align-items:flex-start;gap:10px;margin-bottom:24px}
.contact-row .ic{width:20px;height:20px;border:2px solid var(--ink);border-radius:50%;flex:none;margin-top:2px}
.bottom-bar{top:4787px;left:0;width:1200px;height:39px;background:var(--green-dark);color:#fff;font-size:11px;text-align:center;line-height:39px;letter-spacing:.5px}
</style>
</head>
<body>

<header class="abs site-header">
  <svg class="abs" style="left:40px;top:42px" width="22" height="20" viewBox="0 0 22 20"><path d="M11 1 1 10h3v9h5v-6h4v6h5v-9h3z" fill="var(--green-dark)"/></svg>
  <div class="abs" style="left:88px;top:36px;width:1px;height:34px;background:var(--line)"></div>
  <nav class="nav nav-left"><span>Loan Programs</span><span>Case Studies</span><span>Partners</span></nav>
  <div class="brand">Brevand Finance</div>
  <nav class="nav nav-right"><span>Insights</span><span>About</span><span>Contact</span><span class="apply">Apply Now</span></nav>
</header>

<div class="abs hero" role="img" aria-label="Aerial photo of a suburban neighborhood with new homes"></div>
<h1 class="abs hero-title">The Leading Premier Lender for Real Estate Investors</h1>
<p class="abs hero-sub">Count on us for your every investment need</p>
<div class="btn" style="left:505px;top:498px">Learn More</div>

<div class="abs loan-card" style="left:55px">
  <span class="pin"></span>
  <svg width="140" height="70" viewBox="0 0 140 70"><path d="M10 45 70 8l60 37" fill="none" stroke="#8e8e8e" stroke-width="10"/><rect x="60" y="38" width="20" height="22" fill="#8e8e8e"/></svg>
  <div class="loan-name">RENTAL</div>
  <p class="loan-desc">Long Term Financing for Single Properties and Portfolios of Single-Family Rentals</p>
</div>
<div class="abs loan-card" style="left:423px">
  <span class="pin"></span>
  <svg width="140" height="70" viewBox="0 0 140 70"><path d="M10 45 70 8l60 37" fill="none" stroke="#8e8e8e" stroke-width="10"/><path d="M30 45v20h80V45" fill="none" stroke="#8e8e8e" stroke-width="6"/></svg>
  <div class="loan-name">FIXNFLIP</div>
  <p class="loan-desc">Short Term Financing for the Purchase and Rehab of Single-Family Properties</p>
</div>
<div class="abs loan-card alt" style="left:788px">
  <span class="pin"></span>
  <svg width="140" height="70" viewBox="0 0 140 70"><path d="M10 45 70 8l60 37" fill="none" stroke="#fff" stroke-width="8"/><g fill="#fff"><rect x="46" y="40" width="12" height="10"/><rect x="64" y="40" width="12" height="10"/><rect x="82" y="40" width="12" height="10"/><rect x="46" y="54" width="12" height="10"/><rect x="64" y="54" width="12" height="10"/><rect x="82" y="54" width="12" height="10"/></g></svg>
  <div class="loan-name">MULTIFAMILY</div>
  <p class="loan-desc">Purchase or Refinance 5+ Unit Properties with Rehab Short Term, Intermediate Financing</p>
</div>

<div class="abs fade-bg" style="top:933px;height:707px" role="img" aria-label="Faded photo of suburban houses"></div>
<h2 class="section-title" style="top:1128px"><span class="mark"></span>A Single Source Financial Partner</h2>

<div class="abs service" style="left:50px">
  <svg width="60" height="60" viewBox="0 0 60 60"><circle cx="30" cy="22" r="13" fill="none" stroke="#222" stroke-width="4"/><rect x="12" y="38" width="36" height="18" rx="8" fill="#222"/></svg>
  <h3>Industry Leading Customer Service</h3>
  <p>Dedicated loan officers guide every borrower from first call to closing day.</p>
</div>
<div class="abs service" style="left:330px">
  <svg width="60" height="60" viewBox="0 0 60 60"><rect x="6" y="6" width="48" height="48" fill="none" stroke="#222" stroke-width="3"/><g stroke="#222" stroke-width="4" fill="none"><path d="M18 48V18M12 24l6-6 6 6M30 48V14M24 20l6-6 6 6M42 48V18M36 24l6-6 6 6"/></g></svg>
  <h3>Competitively Priced</h3>
  <p>Clear rates and fees with no hidden costs, built for active investors.</p>
</div>
<div class="abs service" style="left:610px">
  <svg width="60" height="60" viewBox="0 0 60 60"><path d="M30 8c10 6 10 18 0 24C20 26 20 14 30 8z" fill="#222"/><path d="M6 40q12-4 24 6 12-10 24-6v14H6z" fill="#222"/></svg>
  <h3>Meeting All Your Investment Needs</h3>
  <p>Flexible programs for flips, rentals and portfolios of any size or stage.</p>
</div>
<div class="abs service" style="left:890px">
  <svg width="60" height="60" viewBox="0 0 60 60"><rect x="6" y="8" width="48" height="34" rx="2" fill="none" stroke="#222" stroke-width="3"/><path d="M22 52h16M30 42v10" stroke="#222" stroke-width="3"/><path d="M14 32l10-10 8 6 12-12" fill="none" stroke="#222" stroke-width="3"/></svg>
  <h3>Efficient and Effective Communication</h3>
  <p>Fast answers by phone, email or portal so your deal keeps moving.</p>
</div>
<div class="btn" style="left:505px;top:1446px">Apply Now</div>

<h2 class="section-title" style="top:1707px"><span class="mark"></span>Case Studies</h2>
<article class="abs case" style="left:46px">
  <div class="photo" role="img" aria-label="Photo of a large villa with a pool" style="background:linear-gradient(180deg,#5f93d6,#b9a78d 60%,#5a7e8a)"></div>
  <h4>Hamptons, NY</h4>
  <p>Purchase and rehab loan closed in ten days for a waterfront flip, sold for a profit.</p>
</article>
<article class="abs case" style="left:420px">
  <div class="photo" role="img" aria-label="Photo of a large two-story home with lawn" style="background:linear-gradient(180deg,#4c82c9,#b8b2a3 55%,#5d7f45)"></div>
  <h4>Los Angeles, CA</h4>
  <p>Bridge loan funded a full renovation of a hillside home, resold within eight months.</p>
</article>
<article class="abs case" style="left:794px">
  <div class="photo" role="img" aria-label="Photo of a blue house at dusk" style="background:linear-gradient(180deg,#7b8fd6,#3d5a9a 55%,#556a4a)"></div>
  <h4>Cleveland, OH</h4>
  <p>Rental refinance freed cash for a seasoned investor to grow a local portfolio.</p>
</article>
<div class="btn" style="left:505px;top:2157px">Learn More</div>

<div class="abs testimonial-bg" role="img" aria-label="Faded photo of happy clients"></div>
<h2 class="section-title" style="top:2418px"><span class="mark"></span>Client Testimonials</h2>
<div class="abs quote" style="left:75px"><span class="qmark">“</span>Fast approval and clear terms. The team closed my first flip on time and kept me informed.</div>
<div class="abs quote" style="left:430px"><span class="qmark">“</span>They understood my renovation plan and funded draws quickly. I will use them for every deal.</div>
<div class="abs quote" style="left:786px"><span class="qmark">“</span>Great rates on my rental portfolio and a smooth process from application to closing.</div>
<div class="abs person" style="left:90px">Marla Penrose</div>
<div class="abs avatar" role="img" aria-label="Client portrait" style="left:300px"></div>
<div class="abs person" style="left:440px">Tessa Varnell</div>
<div class="abs avatar" role="img" aria-label="Client portrait" style="left:652px"></div>
<div class="abs person" style="left:795px">Dorian Keswick</div>
<div class="abs avatar" role="img" aria-label="Client portrait" style="left:1006px"></div>

<h2 class="section-title" style="top:2933px"><span class="mark"></span>Investor Resources</h2>
<article class="abs resource" style="left:48px;top:3008px;width:554px;height:418px">
  <div class="photo" role="img" aria-label="Photo of a modern glass office building" style="height:310px;background:linear-gradient(160deg,#4f86c8,#9ab0c8 50%,#44586c)"></div>
  <h4>Resource #1</h4>
  <p>A step-by-step guide to estimating rehab costs and building a realistic budget for your next flip.</p>
</article>
<article class="abs resource" style="left:614px;top:3008px;width:538px;height:204px">
  <div class="photo" role="img" aria-label="Photo of a bright living room" style="height:120px;background:linear-gradient(90deg,#c8c2b8,#e6e1d8 50%,#b34a3a)"></div>
  <h4>Resource #2</h4>
  <p>How to read a market before you buy and pick neighborhoods that resell fast.</p>
</article>
<article class="abs resource" style="left:614px;top:3222px;width:538px;height:204px">
  <div class="photo" role="img" aria-label="Photo of a renovated kitchen" style="height:120px;background:linear-gradient(90deg,#c9a77a,#e8dccb 50%,#a98a63)"></div>
  <h4>Resource #3</h4>
  <p>Tips for managing contractors, timelines and draws during a renovation.</p>
</article>
<div class="btn" style="left:505px;top:3474px">Learn More</div>

<div class="abs fade-bg" style="top:3635px;height:725px" role="img" aria-label="Faded photo of a residential street"></div>
<h2 class="section-title" style="top:3734px"><span class="mark"></span>Frequently Asked Questions</h2>
<div class="abs faq" style="top:3813px">
  <div class="faq-q">Do you lend on owner-occupied houses?</div>
  <div class="faq-open"><b>Do you provide proof of fund letters?</b><span>Yes, you can get pre-approved for our hard money loans and rental financing on our website. It takes 24 hours or less.</span></div>
  <div class="faq-q">Do you lend to foreign investors?</div>
  <div class="faq-q">How does my credit score affect the approval of my application?</div>
  <div class="faq-q">Can I pay down my loan principal?</div>
  <div class="faq-q">Is an appraisal always required to fund a loan?</div>
  <div class="faq-q">How are construction draws handled?</div>
  <div class="faq-q">Can I cross-collateralize properties to lower my down payment at closing?</div>
  <div class="faq-q">When will you lend in our area?</div>
  <div class="faq-q">Do you lend on commercial properties?</div>
</div>

<footer class="abs site-footer" style="height:330px">
  <div class="f-col" style="left:60px;top:50px"><div class="brand-lg" style="font-weight:700;color:var(--green-dark)">Brevand Finance</div></div>
  <div class="f-col" style="left:330px"><h5>Quick Links</h5>Home<br>Loan Programs<br>Case Studies<br>Partners<br>Insights<br>About<br>Contact<br>Apply Now</div>
  <div class="f-col" style="left:488px"><h5>Loan Programs</h5>Rental<br>FixNFlip<br>MultiFamily</div>
  <div class="f-col" style="left:680px"><h5>Newsletter</h5><div class="newsletter"><div class="field">Enter Email Address</div><div class="go">SIGN UP</div></div></div>
  <div class="f-col" style="left:966px"><h5>Contact</h5>
    <div class="contact-row"><span class="ic"></span><span>BREVAND FINANCE<br>48 Larkmere Ave<br>New York City, NY 10021</span></div>
    <div class="contact-row"><span class="ic"></span><span>1.800.555.0142</span></div>
    <div class="contact-row"><span class="ic"></span><span>info@brevandfinance.com</span></div>
  </div>
</footer>
<div class="abs bottom-bar">© COPYRIGHT 2017 BREVAND FINANCE. ALL RIGHTS RESERVED</div>

</body>
</html>
```